velmu GmbH needs great looking businesscards to leave an impression

Dear Designers,

Our company velmu GmbH based in switzerland needs to have impressive businesscards. We produce and sell high quality bleaching products for the upper market.
We'd like to have a minimalistic but still meaningful design. You'll fine our company logo attached and some of our packaging designs. Our company slogan is "Brighten your smile". If you need additional information feel free to contact us.
Kind Regards Dano

Dear Designers, This is a business card design contest! I try to call the support to fix that. Kind Regards Dano

```html
<!DOCTYPE html>
<html lang="en">
<head>
<meta charset="utf-8">
<title>velmu GmbH – Business Card</title>
<link rel="stylesheet" href="https://fonts.googleapis.com/css2?family=Open+Sans:wght@300;400&display=swap">
<style>
  :root {
    --pink: #d96f93;
    --mauve: #9a6478;
    --grey: #5e5a66;
    --slate: #3f565b;
    --deep-teal: #22484a;
    --teal: #1a5a5e;
    --ink: #000;
    --paper: #fff;
  }
  * { margin: 0; padding: 0; box-sizing: border-box; }
  html, body {
    width: 1200px; height: 1000px; overflow: hidden;
    background: var(--paper);
    font-family: "Open Sans", sans-serif;
  }
  .canvas { position: relative; width: 1200px; height: 1000px; }
  .card {
    position: absolute; left: 194px; width: 702px;
    border: 6px solid var(--ink); background: var(--paper);
  }
  .card--front { top: 44px; height: 458px; }
  .card--back { top: 560px; height: 418px; }

  .brand {
    position: absolute; left: 18px; top: 34px;
    display: flex; align-items: center; gap: 10px;
  }
  .brand__dot { width: 44px; height: 44px; border-radius: 50%; background: var(--teal); }
  .brand__name {
    font-weight: 300; font-size: 46px; line-height: 1;
    color: var(--teal); letter-spacing: 1px;
  }

  .slogan {
    position: absolute; left: 415px; top: 392px; width: 277px; height: 21px;
    background: linear-gradient(90deg,
      var(--teal) 0 93px, var(--slate) 93px 142px,
      var(--grey) 142px 190px, var(--mauve) 190px 240px, var(--pink) 240px 100%);
    color: var(--paper);
    font-size: 16px; line-height: 21px; letter-spacing: 2.6px;
    padding-left: 31px; white-space: nowrap;
  }

  .contact {
    position: absolute; left: 421px; top: 283px; list-style: none;
  }
  .contact__item {
    display: flex; align-items: center; height: 16.8px;
    font-size: 14px; letter-spacing: 2.4px; white-space: nowrap;
  }
  .contact__item::before {
    content: ""; width: 16px; height: 16px; border-radius: 50%;
    background: currentColor; margin-right: 12px; flex: none;
  }
  .contact__item--company { color: var(--pink); }
  .contact__item--name { color: var(--mauve); }
  .contact__item--street { color: var(--grey); }
  .contact__item--city { color: var(--slate); }
  .contact__item--phone { color: var(--deep-teal); }
  .contact__item--email { color: var(--teal); }
</style>
</head>
<body>
<div class="canvas">
  <section class="card card--front">
    <div class="brand">
      <span class="brand__dot"></span>
      <span class="brand__name">velmu</span>
    </div>
    <p class="slogan">Brighten your smile</p>
  </section>

  <section class="card card--back">
    <ul class="contact">
      <li class="contact__item contact__item--company">velmu GmbH</li>
      <li class="contact__item contact__item--name">Mr Lukas Ferrant</li>
      <li class="contact__item contact__item--street">Lindenhofweg 8</li>
      <li class="contact__item contact__item--city">8805 Seewil</li>
      <li class="contact__item contact__item--phone">+41 79 555 40 40</li>
      <li class="contact__item contact__item--email">lukas.ferrant@velmu.ch</li>
    </ul>
  </section>
</div>
</body>
</html>
```